Wine label Design

We are looking to develop an elegant contemporary Chilean design; for a new Wine Brand ZORIVEN to be sold in Chinese Market.
We would like to see designs that are a fine balance between having a traditional design that can offer quality reassurance and being distinctive enough to stand out on crowded shelves. The final design should be easy-to-remember and communicate Quality, Tradition and have a conection with Chile.

Target Market(s)

Urban Chinese between 25 to 40 yo

Requirements
Must have
• Paper label
Information on Front label : Grape (example Cabernet sauvignon) / Vintage (ex 2010) / Wine of Chile
Bottle shape is given (see attached)
Nice to have
• An element of uniqueness, easy to recall the brand
Red and Gold Color are appreciated by the Target
Should not have
• White background
Number 4 is considered death, should not be included on the design

```html
<!DOCTYPE html>
<html lang="en">
<head>
<meta charset="UTF-8">
<title>ZORIVEN – Cabernet Sauvignon Presentation</title>
<link rel="stylesheet" href="https://fonts.googleapis.com/css2?family=Cinzel:wght@700&family=Marcellus&family=Tinos&display=swap">
<style>
  :root {
    --canvas-bg: #ffffff;
    --paper: #efe4cf;
    --paper-edge: #d6c3a0;
    --frame-line: #8a7a60;
    --wine-red: #b8141b;
    --ink: #1d1410;
    --art-light: #e6dccb;
    --art-mid: #9c8f7c;
    --glass-dark: #4a0508;
    --glass-mid: #a3121a;
    --glass-light: #c94a4a;
    --gold-dark: #8a6a2c;
    --gold-light: #d9b870;
    --collar-band: #121010;
  }
  * { margin: 0; padding: 0; box-sizing: border-box; }
  html, body {
    width: 1200px;
    height: 1019px;
    overflow: hidden;
    background: var(--canvas-bg);
  }
  .canvas { position: relative; width: 1200px; height: 1019px; }

  /* Bottle mockup */
  .bottle { position: absolute; left: 0; top: 0; width: 300px; height: 1019px; }
  .bottle__capsule-name {
    position: absolute; left: 100px; top: 40px; width: 88px;
    text-align: center; font-family: "Cinzel", serif; font-weight: 700;
    font-size: 12px; color: var(--wine-red);
  }
  .bottle-label {
    position: absolute; left: 33px; top: 428px; width: 218px; height: 468px;
    background: radial-gradient(ellipse at center, var(--paper) 55%, var(--paper-edge) 100%);
  }
  .bottle-label__brand {
    position: absolute; top: 36px; width: 100%; text-align: center;
    font-family: "Cinzel", serif; font-weight: 700; font-size: 36px;
    color: var(--wine-red); line-height: 1;
  }
  .bottle-label__scene {
    position: absolute; left: 18px; top: 110px; width: 182px; height: 240px;
    background: linear-gradient(180deg, var(--art-light) 0%, var(--art-mid) 45%, var(--art-light) 100%);
  }
  .bottle-label__grape {
    position: absolute; top: 357px; width: 100%; text-align: center;
    font-family: "Marcellus", serif; font-size: 20px; color: var(--ink);
  }
  .bottle-label__vintage {
    position: absolute; top: 397px; width: 100%; text-align: center;
    font-family: "Tinos", serif; font-size: 19px; color: var(--ink);
  }
  .bottle-label__origin {
    position: absolute; top: 432px; width: 100%; text-align: center;
    font-family: "Marcellus", serif; font-size: 14px; color: var(--ink);
  }
  .accent { color: var(--wine-red); }

  /* Collar panel */
  .collar-name {
    position: absolute; left: 270px; top: 44px; width: 140px; text-align: center;
    font-family: "Cinzel", serif; font-weight: 700; font-size: 16px; color: var(--wine-red);
  }
  .collar { position: absolute; left: 258px; top: 112px; width: 168px; height: 94px; }

  /* Front label */
  .label {
    position: absolute; left: 490px; top: 14px; width: 662px; height: 962px;
    background: radial-gradient(ellipse at center, var(--paper) 55%, var(--paper-edge) 100%);
    box-shadow: 4px 8px 14px rgba(0,0,0,0.35);
  }
  .label__frame { position: absolute; inset: 8px; border: 1px solid var(--frame-line); }
  .label__brand {
    position: absolute; top: 66px; left: 0; width: 100%; text-align: center;
    font-family: "Cinzel", serif; font-weight: 700; font-size: 112px;
    color: var(--wine-red); line-height: 1;
  }
  .label__scene {
    position: absolute; left: 65px; top: 241px; width: 525px; height: 470px;
    background: linear-gradient(180deg, var(--art-light) 0%, var(--art-mid) 45%, var(--art-light) 100%);
  }
  .label__grape {
    position: absolute; top: 738px; left: 0; width: 100%; text-align: center;
    font-family: "Marcellus", serif; font-size: 56px; color: var(--ink);
    text-shadow: 3px 4px 4px rgba(60,20,15,0.4);
  }
  .label__vintage {
    position: absolute; top: 832px; left: 0; width: 100%; text-align: center;
    font-family: "Tinos", serif; font-size: 46px; color: var(--ink);
  }
  .label__origin {
    position: absolute; top: 898px; left: 0; width: 100%; text-align: center;
    font-family: "Marcellus", serif; font-size: 34px; color: var(--ink);
    text-shadow: 2px 3px 3px rgba(60,20,15,0.35);
  }
</style>
</head>
<body>
<main class="canvas">
  <div class="bottle">
    <svg width="300" height="1019" viewBox="0 0 300 1019" role="img" aria-label="Red wine bottle with gold capsule">
      <defs>
        <linearGradient id="glass" x1="0" x2="1" y1="0" y2="0">
          <stop offset="0" stop-color="var(--glass-dark)"/>
          <stop offset="0.35" stop-color="var(--glass-mid)"/>
          <stop offset="0.55" stop-color="var(--glass-light)"/>
          <stop offset="1" stop-color="var(--glass-dark)"/>
        </linearGradient>
        <linearGradient id="gold" x1="0" x2="1" y1="0" y2="0">
          <stop offset="0" stop-color="var(--gold-dark)"/>
          <stop offset="0.5" stop-color="var(--gold-light)"/>
          <stop offset="1" stop-color="var(--gold-dark)"/>
        </linearGradient>
      </defs>
      <path d="M100,30 Q100,18 112,18 L176,18 Q188,18 188,30 L188,210 C188,262 250,282 255,340 L255,960 Q255,990 225,992 L60,992 Q30,990 30,960 L30,340 C35,282 100,262 100,210 Z" fill="url(#glass)"/>
      <rect x="100" y="18" width="88" height="188" rx="8" fill="url(#gold)"/>
      <rect x="100" y="100" width="88" height="70" fill="var(--collar-band)"/>
      <circle cx="144" cy="135" r="28" fill="url(#gold)"/>
    </svg>
    <span class="bottle__capsule-name">ZORIVEN</span>
    <div class="bottle-label">
      <p class="bottle-label__brand">ZORIVEN</p>
      <div class="bottle-label__scene" role="img" aria-label="Etched sepia illustration of drummers before mountain peaks"></div>
      <p class="bottle-label__grape">Cabernet <span class="accent">S</span>auvignon</p>
      <p class="bottle-label__vintage">2010</p>
      <p class="bottle-label__origin">Wine of Chile</p>
    </div>
  </div>

  <span class="collar-name">ZORIVEN</span>
  <svg class="collar" viewBox="0 0 168 94" aria-hidden="true">
    <rect x="2" y="24" width="164" height="46" rx="10" fill="var(--collar-band)" stroke="var(--gold-light)" stroke-width="3"/>
    <circle cx="84" cy="47" r="44" fill="var(--gold-dark)"/>
  </svg>

  <section class="label">
    <div class="label__frame"></div>
    <h1 class="label__brand">ZORIVEN</h1>
    <div class="label__scene" role="img" aria-label="Etched sepia illustration of three drummers in traditional dress in front of Andean mountain peaks"></div>
    <p class="label__grape">Cabernet <span class="accent">S</span>auvignon</p>
    <p class="label__vintage">2010</p>
    <p class="label__origin">Wine of Chile</p>
  </section>
</main>
</body>
</html>
```